Web Site - Holloway-Strength.com

Design a 3 page web site for Holloway Strength. See attached design brief.
Holloway Strength - Web Site
www.holloway-strength.com

Design a 3 page web site for Holloway Strength, a small local fitness center that provided cardio and weights only (machines and free weights). There are no classes or other services offered at this facility. Holloway Strength is an affordable alternative to the big box, expensive fitness centers. It is small, local, convenient and a community oriented place to work out.
web site can be clean, simple and communicate basic information about the company and membership offers. Although the branding is black, orange and gray, the web site colors should be soft, light and neutral colors that will appeal to both men and women.
Text: Input generic text during design for each text area that will be modified later during the coding phase. The selected designer is expected to code the site and deliver all compressive files (images, files and code) for an unrestricted hand off and full ownership of all content by the client for future modifications by others.

Images
Images used can be generic royalty free images of people working out, on cardio machines, lifting on universal equipment, stretching or lifting weights or images with out people i.e a yoga mat, free weights, a row of cardio machines etc. This is an adults only facility - images can be a mix of men and women and of diverse multi ethnic backgrounds. Image of the actual gym are included below but should NOT be used on the web site.

Branding - See attached for vertical and horizontal logos for Holloway Strength. These can be used in any way and should be incorporated into the web site
WEB SITE OUTLINE
THREE web pages - Pages can be individual pages clicked through to each page from a navigation area but ALSO pages can be “blend together” into one long scrolling “home” or primary landing page.
1) Home Page with basic information
2) Membership Page (to be later integrated with Quillmark member software to show changing membership specials). - see example below - all text will change later
3) contact page - address - telephone number - google map directions
www.holloway-strength.com
Address:
Located in Tannery Brook Commons
418 E. Walnut Lane, Suite 305, Alder Falls PA 19399
Tel: 484-555-0172

Target Market(s)

Men and Women - Adults over 18,

Industry/Entity Type

Fitness, Work Out, Gym

Coding

Coded - Design and coding required

Number of Pages Required

3 page

Requirements
Must have
• See Project Brief
Should not have
• Dark Colors that feel too masculine

```html
<!DOCTYPE html>
<html lang="en">
<head>
<meta charset="utf-8">
<title>Contact – Holloway Strength</title>
<link href="https://fonts.googleapis.com/css2?family=Roboto:wght@400;500;700&display=swap" rel="stylesheet">
<style>
  :root {
    --orange: #ff6a00;
    --ink: #222326;
    --text: #4a4b50;
    --muted: #6b6d73;
    --line: #e6e6e9;
    --card: #ffffff;
    --footer: #fafafa;
    --pill: #f1efec;
    --peach: #f8cdb0;
    --cream: #fdf7f2;
  }
  * { box-sizing: border-box; margin: 0; padding: 0; }
  html, body { width: 1200px; height: 807px; overflow: hidden; }
  body {
    font-family: "Roboto", Arial, sans-serif;
    color: var(--text);
    background: var(--footer);
    position: relative;
  }

  /* Header */
  .site-header {
    position: absolute; left: 0; top: 0; width: 1200px; height: 47px;
    background: #fff; border-bottom: 1px solid var(--line);
  }
  .brand { position: absolute; left: 250px; top: 12px; display: flex; align-items: flex-start; gap: 6px; }
  .brand-dot { width: 14px; height: 14px; border-radius: 50%; background: var(--orange); margin-top: 2px; }
  .brand-name { font-size: 10px; font-weight: 500; color: var(--ink); letter-spacing: .2px; line-height: 11px; }
  .brand-tag { font-size: 7px; font-weight: 500; color: var(--muted); line-height: 9px; }
  .nav { position: absolute; left: 550px; top: 9px; display: flex; gap: 8px; }
  .nav a {
    font-size: 10px; font-weight: 500; color: var(--text); text-decoration: none;
    height: 28px; line-height: 28px; padding: 0 8px; border-radius: 14px;
  }
  .nav a.active { background: var(--pill); color: var(--ink); border: 1px solid #ebe7e2; line-height: 26px; }
  .btn {
    display: inline-block; background: var(--orange); color: #fff; font-weight: 700;
    border-radius: 16px; text-align: center; text-decoration: none;
    box-shadow: 0 4px 10px rgba(255,106,0,.25);
  }
  .join { position: absolute; left: 884px; top: 9px; width: 66px; height: 29px; line-height: 29px; font-size: 9.5px; }

  /* Main */
  .main {
    position: absolute; left: 0; top: 47px; width: 1200px; height: 535px;
    background: linear-gradient(180deg, #fafafb 0%, #f2f3f6 100%);
  }
  .page-title { position: absolute; left: 250px; top: 20px; font-size: 22px; font-weight: 500; color: var(--ink); }
  .page-lead { position: absolute; left: 250px; top: 51px; font-size: 10px; color: var(--text); }

  .card {
    position: absolute; top: 75px; width: 345px; height: 358px;
    background: var(--card); border: 1px solid var(--line); border-radius: 10px;
  }
  .card.form-card { left: 250px; }
  .card.map-card { left: 605px; background: linear-gradient(160deg, #fafafb, #f3f4f6); }

  .info { position: absolute; left: 12px; font-size: 7.8px; line-height: 12.5px; color: var(--text); }
  .info b { font-weight: 500; color: var(--ink); }
  .info .ico { position: absolute; left: 0; top: 1px; width: 10px; height: 10px; }
  .info .txt { margin-left: 17px; }
  .divider { position: absolute; left: 12px; right: 12px; top: 96px; height: 1px; background: var(--line); }
  .label { position: absolute; left: 12px; font-size: 7.8px; font-weight: 500; color: var(--ink); }
  .field {
    position: absolute; left: 12px; width: 321px; border: 1px solid #e1e1e5; border-radius: 6px;
    background: #fff; font-size: 9.5px; color: var(--muted); padding: 0 8px;
  }
  .send { position: absolute; left: 12px; top: 309px; width: 82px; height: 25px; line-height: 25px; font-size: 8.5px; border-radius: 13px; }
  .form-note { position: absolute; left: 12px; top: 339px; font-size: 7.5px; color: var(--muted); }

  .map-title { position: absolute; top: 58px; width: 100%; text-align: center; font-size: 10px; font-weight: 500; color: #55565b; }
  .map-hint { position: absolute; top: 169px; width: 100%; text-align: center; font-size: 7.8px; line-height: 13px; color: var(--muted); }
  .map-hint b { font-weight: 500; color: #3f4045; }
  .map-link { position: absolute; top: 290px; width: 100%; text-align: center; font-size: 10px; font-weight: 500; color: var(--orange); text-decoration: none; }

  .visit-band {
    position: absolute; left: 250px; top: 445px; width: 700px; height: 65px;
    border: 1px solid #f6dccb; border-radius: 12px;
    background: linear-gradient(100deg, var(--peach) 0%, #fbe3d2 35%, var(--cream) 52%, #fff 100%);
  }
  .visit-title { position: absolute; left: 14px; top: 14px; font-size: 12.5px; font-weight: 700; color: var(--ink); }
  .visit-text { position: absolute; left: 14px; top: 35px; font-size: 10px; color: #55565b; }
  .call { position: absolute; left: 577px; top: 17px; width: 109px; height: 29px; line-height: 29px; font-size: 9.5px; }

  /* Footer */
  .site-footer {
    position: absolute; left: 0; top: 582px; width: 1200px; height: 225px;
    background: var(--footer); border-top: 1px solid var(--line);
  }
  .f-brand { position: absolute; left: 250px; top: 17px; }
  .f-about { position: absolute; left: 250px; top: 44px; width: 270px; font-size: 7.8px; line-height: 13px; color: var(--text); }
  .f-col { position: absolute; font-size: 7.8px; line-height: 12.5px; color: var(--text); }
  .f-col b { font-weight: 500; color: var(--ink); }
  .f-col .ico { position: absolute; left: 0; top: 1px; width: 10px; height: 10px; }
  .f-col .txt { margin-left: 17px; }
  .f-head { font-size: 7.5px; font-weight: 500; color: #3f4045; }
  .f-rule { position: absolute; left: 250px; width: 700px; top: 129px; height: 1px; background: var(--line); }
  .copy { position: absolute; left: 250px; top: 140px; font-size: 7.8px; color: var(--text); }
</style>
</head>
<body>

<header class="site-header">
  <div class="brand">
    <span class="brand-dot"></span>
    <div>
      <div class="brand-name">HOLLOWAY STRENGTH</div>
      <div class="brand-tag">Cardio • Machines • Free Weights</div>
    </div>
  </div>
  <nav class="nav">
    <a href="#">Home</a>
    <a href="#">Membership</a>
    <a href="#" class="active">Contact</a>
  </nav>
  <a href="#" class="btn join">Join Now</a>
</header>

<main class="main">
  <h1 class="page-title">Contact</h1>
  <p class="page-lead">Get directions, ask about membership, or send us a quick note.</p>

  <section class="card form-card">
    <div class="info" style="top:14px">
      <svg class="ico" viewBox="0 0 24 24" fill="none" stroke="#3a3b40" stroke-width="2"><path d="M12 22s7-6.5 7-12a7 7 0 0 0-14 0c0 5.5 7 12 7 12z"/><circle cx="12" cy="10" r="2.5"/></svg>
      <div class="txt"><b>Located in Tannery Brook Commons</b><br>418 E. Walnut Lane, Suite 305<br>Alder Falls, PA 19399</div>
    </div>
    <div class="info" style="top:57px">
      <svg class="ico" viewBox="0 0 24 24" fill="none" stroke="#3a3b40" stroke-width="2"><path d="M5 3h4l2 5-2.5 1.5a11 11 0 0 0 6 6L16 13l5 2v4a2 2 0 0 1-2 2A17 17 0 0 1 3 5a2 2 0 0 1 2-2z"/></svg>
      <div class="txt"><b>Tel</b> 484-555-0172</div>
    </div>
    <div class="info" style="top:75px">
      <svg class="ico" viewBox="0 0 24 24" fill="none" stroke="#ff6a00" stroke-width="2"><rect x="3" y="5" width="18" height="14" rx="2"/><path d="M3 7l9 6 9-6"/></svg>
      <div class="txt"><b>Email</b> hello@holloway-strength.com (placeholder)</div>
    </div>
    <div class="divider"></div>

    <label class="label" style="top:108px">Name</label>
    <div class="field" style="top:122px;height:30px;line-height:28px">Your name</div>
    <label class="label" style="top:160px">Email</label>
    <div class="field" style="top:174px;height:30px;line-height:28px">you@example.com</div>
    <label class="label" style="top:213px">Message</label>
    <div class="field" style="top:227px;height:76px;padding-top:8px">How can we help?</div>

    <a href="#" class="btn send">Send Message</a>
    <p class="form-note">Form is a placeholder. Wire to your preferred email service during development.</p>
  </section>

  <section class="card map-card">
    <div class="map-title">Map Embed Placeholder</div>
    <div class="map-hint">Replace this block with an iframe embed for:<br><b>418 E. Walnut Lane, Suite 305, Alder Falls PA 19399</b></div>
    <a href="#" class="map-link">Open in Map App</a>
  </section>

  <section class="visit-band">
    <h2 class="visit-title">Prefer to stop by?</h2>
    <p class="visit-text">We’re in Tannery Brook Commons. Call ahead if you’d like a quick walk-through.</p>
    <a href="#" class="btn call">Call 484-555-0172</a>
  </section>
</main>

<footer class="site-footer">
  <div class="brand f-brand">
    <span class="brand-dot"></span>
    <div>
      <div class="brand-name">HOLLOWAY STRENGTH</div>
      <div class="brand-tag">Small. Local. Convenient.</div>
    </div>
  </div>
  <p class="f-about">Affordable cardio and weights only. No classes. No upsells. Just a clean, welcoming place to work out.</p>

  <div class="f-col" style="left:541px;top:17px">
    <svg class="ico" viewBox="0 0 24 24" fill="none" stroke="#3a3b40" stroke-width="2"><path d="M12 22s7-6.5 7-12a7 7 0 0 0-14 0c0 5.5 7 12 7 12z"/><circle cx="12" cy="10" r="2.5"/></svg>
    <div class="txt"><b>Located in Tannery Brook Commons</b><br>418 E. Walnut Lane, Suite 305<br>Alder Falls, PA 19399</div>
  </div>
  <div class="f-col" style="left:541px;top:84px">
    <svg class="ico" viewBox="0 0 24 24" fill="none" stroke="#3a3b40" stroke-width="2"><path d="M5 3h4l2 5-2.5 1.5a11 11 0 0 0 6 6L16 13l5 2v4a2 2 0 0 1-2 2A17 17 0 0 1 3 5a2 2 0 0 1 2-2z"/></svg>
    <div class="txt"><b>Tel</b> 484-555-0172</div>
  </div>

  <div class="f-col" style="left:750px;top:25px;width:200px">
    <div class="f-head">Hours</div>
    <div>Mon–Fri: 5am–10pm</div>
    <div>Sat–Sun: 7am–8pm</div>
    <div class="f-head" style="margin-top:9px">Note</div>
    <div>Hours and membership details can be updated during buildout.</div>
  </div>

  <div class="f-rule"></div>
  <p class="copy">© 2026 Holloway Strength. All rights reserved.</p>
</footer>

</body>
</html>
```